Financial services firm needs updated web design

Our current website, coinpathwealth.example was created by ourselves using templates provided by our website host, Harborline Webworks. We are looking to get a whole new look and feel to our website that is clean, professional and easy to navigate. The design must be able to be transferred to Harborline Webworks for hosting (FTP??-outside my area of expertise - sorry) and that the information can be updated and changed by ourselves in the future. I have included our updated logo and our business card design.
Updates
Project Deadline Extended
Reason: Went away on vacation for two weeks.
Target Market(s)
Age 50+ individuals looking for investment, retirement and estate planning guidance.
Industry/Entity Type
Financial
Number of Pages Required
1 page
Font styles to use
Other font styles liked:
- Adobe Caslon Pro
Look and feel
Each slider illustrates characteristics of the customer's brand and the style your logo design should communicate.

```html
<!DOCTYPE html>
<html lang="en">
<head>
<meta charset="utf-8">
<title>Alder Ridge Advisors</title>
<link href="https://fonts.googleapis.com/css2?family=Open+Sans:wght@400;600;700&family=Sansita:wght@800&display=swap" rel="stylesheet">
<style>
:root{
  --green:#2f6b33;
  --green-dark:#255a29;
  --ink:#333;
  --muted:#555;
  --grey:#a9a9a9;
  --grey-light:#e4e4e4;
  --white:#fff;
  --black:#111;
}
*{margin:0;padding:0;box-sizing:border-box}
html,body{width:696px;height:1200px;overflow:hidden;background:var(--white);font-family:"Open Sans",sans-serif;color:var(--ink)}
.page{position:relative;width:696px;height:1200px}
.abs{position:absolute}

.brand{left:58px;top:44px;font-size:16px;font-weight:600;color:var(--ink);display:flex;align-items:center;gap:7px;white-space:nowrap}
.brand-mark{width:10px;height:10px;background:var(--green)}
.contact-lines{left:350px;top:16px;font-size:8px;line-height:11px;color:var(--muted)}
.phone-lines{left:554px;top:16px;font-size:8px;line-height:11px;color:var(--muted)}
.icon-mail{left:510px;top:20px}
.icon-phone{left:623px;top:17px}
.btn-contact{left:561px;top:51px;width:78px;height:17px;background:var(--green);color:var(--white);font-size:8px;text-align:center;line-height:15px;border-top:2px solid #4a8a4e}

.nav{left:0;top:80px;width:696px;height:27px;background:var(--green);display:flex;padding-left:58px}
.nav a{color:var(--white);font-size:7.5px;text-decoration:none;line-height:27px;padding:0 10px;border-right:1px solid #3e7c42;white-space:nowrap}
.nav a.active{background:var(--black)}

.hero{left:0;top:107px;width:696px;height:317px;background:linear-gradient(120deg,#e8eee0 0%,#c9dba8 40%,#9fc36a 70%,#4d7d2e 100%)}
.hero-arrow{top:244px}
.hero-box{left:217px;top:190px;width:264px;height:165px;background:rgba(25,25,25,.78);text-align:center;color:var(--white)}
.hero-box h1{font-family:"Sansita",sans-serif;font-weight:800;font-size:21px;line-height:24px;margin-top:18px;letter-spacing:.5px}
.hero-box p{font-size:7px;line-height:14px;margin:14px 18px 0}
.hero-btns{display:flex;gap:4px;justify-content:center;margin-top:12px}
.hero-btns span{width:76px;height:20px;font-size:7.5px;line-height:20px}
.btn-green{background:var(--green)}
.btn-ghost{border:1px solid #ccc}
.dots{left:333px;top:432px;display:flex;gap:3px}
.dots i{width:5px;height:5px;background:#bbb}
.dots i:first-child{background:var(--green)}

.welcome{left:64px;top:456px;width:568px;text-align:center}
.welcome h2,.services-title{font-size:14.5px;font-weight:600;color:#3a3a3a}
.welcome p{font-size:7.6px;line-height:10.5px;color:var(--muted);margin-top:10px}
.btn-dark{left:318px;top:526px;width:67px;height:17px;background:var(--black);color:var(--white);font-size:8px;line-height:17px;text-align:center}
.services-title{left:0;width:696px;top:579px;text-align:center}

.service{width:170px}
.service .ic{position:absolute;left:0;top:0;width:30px;height:30px;background:var(--green);display:flex;align-items:center;justify-content:center}
.service .ic::after{content:"";position:absolute;bottom:-4px;left:11px;border:4px solid transparent;border-top-color:var(--green);border-bottom:0}
.service h3{margin-left:40px;font-size:11px;font-weight:400;line-height:14px;color:#333;min-height:30px}
.service p{font-size:7px;line-height:9.8px;color:var(--muted);margin-top:11px}
.service a{display:block;font-size:7px;color:var(--green);margin-top:6px;text-decoration:none}

.widgets{left:58px;top:866px;width:580px;height:225px;background:#f3f3f3;border-top:3px solid #222}
.w-head{height:30px;display:flex;align-items:center;background:var(--white)}
.w-head .ic{width:36px;height:30px;display:flex;align-items:center;justify-content:center}
.w-head h4{font-size:14px;font-weight:400;margin-left:12px;color:#222;white-space:nowrap}
.calc{left:0;top:17px;width:172px}
.calc .ic{background:var(--grey-light)}
.calc-body{margin-top:10px;height:148px;background:var(--grey);padding:9px 10px}
.calc-row{display:flex;justify-content:space-between;align-items:center;height:17.6px;font-size:7.5px;color:var(--white)}
.calc-row span:last-child{width:50px;height:14px;background:var(--white);color:#333;font-size:7px;padding-left:4px;line-height:14px}
.calc-btns{display:flex;justify-content:flex-end;gap:5px;margin-top:16px}
.calc-btns span{width:50px;height:15px;font-size:8px;line-height:15px;text-align:center;color:var(--white)}
.posts{left:203px;top:17px;width:172px}
.posts .ic{background:var(--green)}
.post{background:var(--white);margin-top:2px;border-bottom:1px solid #ddd}
.post-body{display:flex;height:55px;border-bottom:1px solid #ddd}
.post-date{width:36px;flex:none;text-align:center;border-right:1px solid #ddd;padding-top:6px;color:#555}
.post-date b{display:block;font-size:15px;font-weight:400;line-height:16px}
.post-date small{font-size:5.5px;display:block;line-height:7px}
.post-body p{font-size:6px;line-height:10.4px;color:#888;padding:6px 8px;overflow:hidden}
.post-meta{height:23px;font-size:7px;line-height:23px;padding-left:12px;color:#333;position:relative}
.post-meta u{text-decoration:underline}
.news{left:391px;top:17px;width:171px}
.news .ic{background:var(--grey)}
.news-body{margin-top:10px;height:148px;background:var(--grey);padding:14px 14px;text-align:center;color:var(--white)}
.news-body h5{font-size:10px;line-height:14.5px;font-weight:700}
.news-body p{font-size:6.5px;font-weight:700;margin-top:10px}
.news-input{margin-top:14px;height:19px;background:var(--white);color:#777;font-size:7.5px;line-height:19px;text-align:left;padding-left:8px}
.news-btn{margin-top:14px;height:19px;background:var(--green);font-size:9px;font-weight:700;line-height:19px}

.footer{left:0;top:1127px;width:696px;height:73px;background:var(--green-dark);color:var(--white)}
.foot-nav{left:58px;top:24px;font-size:7.5px;word-spacing:1px}
.foot-copy{left:58px;top:44px;font-size:7.5px}
.foot-copy em{font-style:normal;color:#e6c82a}
.social{left:571px;top:27px;display:flex;gap:12px}
.social i{width:15px;height:15px;border-radius:50%;background:var(--white)}
</style>
</head>
<body>
<div class="page">
  <header>
    <div class="abs brand"><span class="brand-mark"></span>Alder Ridge Advisors</div>
    <div class="abs contact-lines">advisor@coinpathwealth.example<br>www.coinpathwealth.example</div>
    <svg class="abs icon-mail" width="16" height="12" viewBox="0 0 16 12"><rect x="1" y="1" width="14" height="10" fill="none" stroke="#2f6b33" stroke-width="1.6"/><path d="M1 1l7 6 7-6M1 11l5-5M15 11l-5-5" fill="none" stroke="#2f6b33" stroke-width="1.6"/></svg>
    <div class="abs phone-lines">t. 555.010.0144<br>F. 555.010.0147</div>
    <svg class="abs icon-phone" width="16" height="16" viewBox="0 0 16 16"><circle cx="8" cy="8" r="6.5" fill="none" stroke="#2f6b33" stroke-width="1.4"/><path d="M5.5 5c0 3 2.5 5.5 5.5 5.5l.5-1.5-1.5-.8-.7.7c-1-.5-1.7-1.2-2.2-2.2l.7-.7L7 4.5z" fill="#2f6b33"/></svg>
    <div class="abs btn-contact">Contact Us</div>
  </header>

  <nav class="abs nav">
    <a class="active">Home</a><a>Team</a><a>Income for Life</a><a>NEW</a><a>Tax Planning &amp; Tips</a><a>Canadian Mortgage</a><a>Financial Products</a><a>Mutual Funds</a><a style="border:0">Disclosure Notices</a>
  </nav>

  <section class="abs hero" role="img" aria-label="Photo of financial reports with figures, a pen, charts and a calculator in green tones"></section>
  <svg class="abs hero-arrow" style="left:19px" width="22" height="22" viewBox="0 0 22 22"><circle cx="11" cy="11" r="10" fill="rgba(255,255,255,.6)"/><path d="M13 6l-5 5 5 5" fill="none" stroke="#fff" stroke-width="2.5"/></svg>
  <svg class="abs hero-arrow" style="left:652px" width="22" height="22" viewBox="0 0 22 22"><circle cx="11" cy="11" r="10" fill="rgba(255,255,255,.6)"/><path d="M9 6l5 5-5 5" fill="none" stroke="#fff" stroke-width="2.5"/></svg>
  <div class="abs hero-box">
    <h1>Alder Ridge<br>Advisory Service</h1>
    <p>Lorem ipsum dolor sit amet, consectetur adipiscing elit. In faucibus augue id dapibus ultricies. Morbi venenatis</p>
    <div class="hero-btns"><span class="btn-green">View Work</span><span class="btn-ghost">Learn More</span></div>
  </div>
  <div class="abs dots"><i></i><i></i><i></i><i></i></div>

  <section class="abs welcome">
    <h2>Welcome to Our Site</h2>
    <p>Lorem ipsum dolor sit amet, consectetur adipiscing elit. Proin faucibus arcu eget mi pellentesque egestas. Morbi consequat neque id commodo congue. In urna ipsum, rhoncus eget malesuada eu, varius eget dui. Mauris mollis bibendum eleifend. Mauris ex tellus, consectetur ac egestas nec, ornare at est. Nunc quis porttitor nulla. Quisque bibendum massa nibh, nec luctus est dictum ut. Sed sollicitudin ultrices nulla ut venenatis.</p>
  </section>
  <div class="abs btn-dark">Read More</div>

  <h2 class="abs services-title">Our Financial Planning Services</h2>

  <div class="abs service" style="left:58px;top:630px"><span class="ic"><svg width="18" height="18" viewBox="0 0 18 18"><circle cx="9" cy="9" r="7.5" fill="none" stroke="#fff" stroke-width="1.5"/><text x="9" y="13" font-size="11" text-anchor="middle" fill="#fff" font-family="Open Sans">$</text></svg></span><h3>Individual Financial Planning</h3><p>Fusce interdum, neque vitae lacinia mollis, nisi aliquam felis, et tempor nisl ligula vitae urna. In diam, eleifend et turpis a,</p><a>Details ➔</a></div>
  <div class="abs service" style="left:265px;top:630px"><span class="ic"><svg width="16" height="16" viewBox="0 0 16 16"><circle cx="8" cy="5" r="3" fill="#fff"/><path d="M2 15c0-4 3-6 6-6s6 2 6 6z" fill="#fff"/></svg></span><h3>Business Planning Services</h3><p>Fusce interdum, neque vitae lacinia mollis, nisi aliquam felis, et tempor nisl ligula vitae urna. In diam, eleifend et turpis a,</p><a>Details ➔</a></div>
  <div class="abs service" style="left:473px;top:630px"><span class="ic"><svg width="16" height="18" viewBox="0 0 16 18"><text x="8" y="15" font-size="16" text-anchor="middle" fill="#fff" font-family="Open Sans">$</text></svg></span><h3>Financial Security Planning</h3><p>Fusce interdum, neque vitae lacinia mollis, nisi aliquam felis, et tempor nisl ligula vitae urna. In diam, eleifend et turpis a,</p><a>Details ➔</a></div>
  <div class="abs service" style="left:58px;top:740px"><span class="ic"><svg width="18" height="18" viewBox="0 0 18 18"><circle cx="7" cy="11" r="5" fill="none" stroke="#fff" stroke-width="1.8"/><path d="M10 8l6-6M12 2h4v4" fill="none" stroke="#fff" stroke-width="1.8"/></svg></span><h3>Investment Planning</h3><p>Fusce interdum, neque vitae lacinia mollis, nisi aliquam felis, et tempor nisl ligula vitae urna. In diam, eleifend et turpis a,</p><a>Details ➔</a></div>
  <div class="abs service" style="left:265px;top:740px"><span class="ic"><svg width="14" height="16" viewBox="0 0 14 16"><rect x="1" y="2" width="12" height="13" fill="none" stroke="#fff" stroke-width="1.5"/><rect x="4" y="0.5" width="6" height="3" fill="#fff"/><path d="M4 7h6M4 10h6M4 13h4" stroke="#fff" stroke-width="1.2"/></svg></span><h3>Retirement Planning Services</h3><p>Fusce interdum, neque vitae lacinia mollis, nisi aliquam felis, et tempor nisl ligula vitae urna. In diam, eleifend et turpis a,</p><a>Details ➔</a></div>
  <div class="abs service" style="left:473px;top:740px"><span class="ic"><svg width="18" height="16" viewBox="0 0 18 16"><rect x="1" y="2" width="12" height="10" fill="none" stroke="#fff" stroke-width="1.5"/><path d="M4 6h6M4 9h4M12 14l5-5" stroke="#fff" stroke-width="1.5"/></svg></span><h3>Tax &amp; Estate Planning</h3><p>Fusce interdum, neque vitae lacinia mollis, nisi aliquam felis, et tempor nisl ligula vitae urna. In diam, eleifend et turpis a,</p><a>Details ➔</a></div>

  <section class="abs widgets">
    <div class="abs calc">
      <div class="w-head"><span class="ic"><svg width="14" height="16" viewBox="0 0 14 16"><rect x="1" y="1" width="12" height="14" fill="none" stroke="#999" stroke-width="1.2"/><path d="M3 4h8M3 7h2M6 7h2M9 7h2M3 10h2M6 10h2M9 10h2M3 13h2M6 13h2M9 13h2" stroke="#999" stroke-width="1.2"/></svg></span><h4>Calculator</h4></div>
      <div class="calc-body">
        <div class="calc-row"><span>Payment Per Year</span><span>12</span></div>
        <div class="calc-row"><span>Loan Amount</span><span>12</span></div>
        <div class="calc-row"><span>Interest Rate</span><span>12</span></div>
        <div class="calc-row"><span>Periodic Payment</span><span>12</span></div>
        <div class="calc-row"><span>Number of Payment</span><span>360</span></div>
        <div class="calc-btns"><span style="background:#2a2222">Clear</span><span style="background:var(--green)">Calculate</span></div>
      </div>
    </div>
    <div class="abs posts">
      <div class="w-head"><span class="ic"><svg width="16" height="14" viewBox="0 0 16 14"><path d="M1 2h6v11H1zM9 2h6v11H9z" fill="none" stroke="#fff" stroke-width="1.4"/><path d="M2.5 5h3M2.5 8h3M10.5 5h3M10.5 8h3" stroke="#fff"/></svg></span><h4>Recent Posts</h4></div>
      <div class="post"><div class="post-body"><div class="post-date"><b>08</b><small>MAY</small><small>2012</small></div><p>Etiam porta sem malesuada magna mollis euismod. Aenean eu leo quam magna maen Ornare Fusce Magna Cras Ullamcorper ...</p></div><div class="post-meta">By <u>Alex Reed</u> / 7 Comments<svg class="abs" style="right:8px;top:5px" width="13" height="13" viewBox="0 0 13 13"><circle cx="6.5" cy="6.5" r="6.5" fill="#111"/><path d="M6.5 3.5v6M3.5 6.5h6" stroke="#fff" stroke-width="1.4"/></svg></div></div>
      <div class="post"><div class="post-body"><div class="post-date"><b>23</b><small>AUG</small><small>2012</small></div><p>lit nulls commodo, tortor mauris condimecommodo, tortor mauris condimentum nibh, ut fermentum massa justo sit amet ri ...</p></div><div class="post-meta">By <u>Dana Holt</u> / 2 Comments</div></div>
    </div>
    <div class="abs news">
      <div class="w-head"><span class="ic"><svg width="18" height="14" viewBox="0 0 18 14"><path d="M2 5h4l8-4v12l-8-4H2z" fill="#fff"/></svg></span><h4>Newsletter signup</h4></div>
      <div class="news-body">
        <h5>SUSCRIBE TO OUR<br>NEWSLETTER</h5>
        <p>Enter your email to join our mailing list.</p>
        <div class="news-input">Enter your email id</div>
        <div class="news-btn">SUBMIT</div>
      </div>
    </div>
  </section>

  <footer class="abs footer">
    <div class="abs foot-nav">Home &nbsp; | &nbsp; Team &nbsp; | &nbsp; Income for Life &nbsp; | &nbsp; NEW &nbsp; | &nbsp; Tax Planning &amp; Tips &nbsp; | &nbsp; Canadian Mortgage</div>
    <div class="abs foot-copy">Copyright © <em>yourwebsite</em> &nbsp;| &nbsp;Terms &amp; Conditions &nbsp;| &nbsp;Privacy Policy</div>
    <div class="abs social"><i></i><i></i><i></i></div>
  </footer>
</div>
</body>
</html>
```